Tradeshwo display 8x10 high resolution backdrop

I created a backdrop I wanted to use via Chat GPT but the image isn't high quality enough for print so I want someone to recreate it as close as possible to my creation. See attached, TY!

```html
<!DOCTYPE html>
<html lang="en">
<head>
<meta charset="utf-8">
<title>Harborline Flow Systems – Tradeshow Backdrop</title>
<link href="https://fonts.googleapis.com/css2?family=Anton&family=Oswald:wght@500;600&family=Montserrat:wght@400;700;800&family=Barlow:wght@400;600;700&family=Barlow+Condensed:wght@600;700&display=swap" rel="stylesheet">
<style>
  :root{
    --stage:#8f9094;
    --navy:#24398a;
    --navy-deep:#0c1a3f;
    --blue:#1466c0;
    --blue-light:#1a8ad6;
    --cyan:#2aa9e6;
    --ink:#0b0b0b;
    --text:#2a2a2a;
    --divider:#d7dae0;
    --white:#ffffff;
  }
  *{margin:0;padding:0;box-sizing:border-box}
  html,body{width:1200px;height:857px;overflow:hidden;background:var(--stage)}
  .backdrop{position:absolute;left:38px;top:0;width:1124px;height:857px;background:var(--white);overflow:hidden}

  .hero-photo{position:absolute;left:0;top:0;width:100%;height:275px;
    background:linear-gradient(180deg,#c9a77e 0%,#8aa0a8 14%,#3f6a3a 30%,#4f7aa0 55%,#6f97b8 75%,#39597a 100%)}

  .brand-card{position:absolute;left:30px;top:30px;width:326px;height:326px;background:var(--white);
    border:3px solid var(--navy-deep);box-shadow:0 8px 14px rgba(0,0,0,.35)}
  .brand-name{position:absolute;left:0;right:0;top:62px;text-align:center;font-family:"Montserrat",sans-serif;
    font-weight:800;color:var(--navy);font-size:40px;line-height:1.05;letter-spacing:1px}
  .brand-name small{display:block;font-size:17px;letter-spacing:2px;margin-top:6px}
  .promise{position:absolute;top:214px;width:80px;text-align:center;transform:translateX(-50%)}
  .promise svg{width:52px;height:52px;display:block;margin:0 auto}
  .promise p{margin-top:14px;font-family:"Montserrat",sans-serif;font-weight:700;font-size:9.5px;line-height:12px;letter-spacing:.8px;color:var(--ink)}
  .promise-rule{position:absolute;top:216px;width:2px;height:92px;background:var(--ink)}

  .headline-top{position:absolute;left:386px;top:296px;font-family:"Anton",sans-serif;font-size:58px;letter-spacing:4px;color:var(--ink);line-height:1}
  .headline-main{position:absolute;left:0;right:0;top:370px;text-align:center;padding-left:12px;font-family:"Anton",sans-serif;font-size:86px;letter-spacing:5px;line-height:1;
    background:linear-gradient(180deg,var(--blue-light),#0a4ea8);-webkit-background-clip:text;background-clip:text;color:transparent}
  .tagline{position:absolute;top:460px;left:172px;right:171px;display:flex;align-items:center;gap:10px;font-family:"Montserrat",sans-serif;font-size:24px;letter-spacing:1.5px;color:var(--ink);white-space:nowrap}
  .tagline::before,.tagline::after{content:"";flex:1;height:2px;background:var(--ink)}

  .industry-band{position:absolute;left:0;top:491px;width:100%;height:39px;background:var(--navy);color:var(--white);
    font-family:"Montserrat",sans-serif;font-weight:700;font-size:19px;letter-spacing:6.2px;line-height:39px;text-align:center;white-space:nowrap}

  .offerings{position:absolute;left:0;top:531px;width:100%;height:215px;display:flex}
  .offering{position:relative;text-align:center;border-right:2px solid var(--divider)}
  .offering:last-child{border-right:none}
  .offering-visual{width:118px;height:124px;margin:10px auto 0;border-radius:6px}
  .offering h3{margin-top:10px;font-family:"Oswald",sans-serif;font-weight:600;font-size:19px;line-height:20px;color:var(--navy);transform:scaleX(.88);white-space:nowrap}
  .offering p{margin-top:2px;font-family:"Barlow",sans-serif;font-size:10.5px;line-height:14px;color:var(--text)}
  .o1{width:209px}.o2{width:178px}.o3{width:182px}.o4{width:176px}.o5{width:182px}.o6{width:197px}
  .visual-steel{background:linear-gradient(160deg,#3a5fd0,#1b3a9c)}
  .visual-grey{background:linear-gradient(160deg,#b8bcc2,#6f7379)}
  .visual-drive{width:80px;background:linear-gradient(160deg,#3a3f48,#1f4a8c)}

  .footer-water{position:absolute;left:0;top:748px;width:100%;height:109px;
    background:linear-gradient(180deg,#2b62c4 0%,#143a86 14%,#0c1f4d 50%,#081636 100%)}
  .service-pin{position:absolute;left:46px;top:781px;width:46px;height:46px}
  .service-label{position:absolute;left:104px;top:773px;font-family:"Barlow Condensed",sans-serif;font-weight:700;font-size:21px;color:var(--cyan);letter-spacing:.5px}
  .service-states{position:absolute;left:104px;top:802px;font-family:"Barlow Condensed",sans-serif;font-weight:700;font-size:15.5px;color:var(--white);letter-spacing:.3px}
  .footer-rule{position:absolute;top:784px;width:2px;height:55px;background:var(--white)}
  .site-url{position:absolute;left:486px;top:795px;font-family:"Barlow",sans-serif;font-weight:700;font-size:24px;color:var(--white)}
  .site-url span{color:var(--cyan)}
  .partner-lead{position:absolute;left:808px;top:781px;font-family:"Barlow Condensed",sans-serif;font-weight:600;font-size:16px;color:var(--white)}
  .partner-line{position:absolute;left:808px;top:799px;font-family:"Barlow Condensed",sans-serif;font-weight:700;font-size:25px;color:var(--cyan);letter-spacing:.5px}
</style>
</head>
<body>
<main class="backdrop">
  <div class="hero-photo" role="img" aria-label="Photo of a water treatment plant with clarifier tanks, walkways and trees at sunset"></div>

  <section class="brand-card">
    <div class="brand-name">HARBORLINE<small>FLOW SYSTEMS</small></div>

    <div class="promise" style="left:35px">
      <svg viewBox="0 0 52 52" fill="none" stroke="#0b0b0b" stroke-width="2"><circle cx="26" cy="21" r="15"/><circle cx="26" cy="21" r="10"/><path d="M21 21l4 4 7-8"/><path d="M17 33l-5 14 7-3 4 6 3-10M35 33l5 14-7-3-4 6-3-10"/></svg>
      <p>QUALITY<br>BRANDS</p>
    </div>
    <div class="promise-rule" style="left:66px"></div>
    <div class="promise" style="left:110px">
      <svg viewBox="0 0 52 52" fill="none" stroke="#0b0b0b" stroke-width="2"><circle cx="26" cy="26" r="17" stroke-dasharray="7 4"/><circle cx="26" cy="26" r="13"/><circle cx="26" cy="26" r="9"/></svg>
      <p>ENGINEERED<br>SOLUTIONS</p>
    </div>
    <div class="promise-rule" style="left:153px"></div>
    <div class="promise" style="left:195px">
      <svg viewBox="0 0 52 52" fill="none" stroke="#0b0b0b" stroke-width="2"><path d="M8 30a18 18 0 0 1 36 0"/><circle cx="26" cy="30" r="12"/><rect x="4" y="26" width="6" height="14" rx="3"/><rect x="42" y="26" width="6" height="14" rx="3"/><path d="M45 40q0 8-12 8"/></svg>
      <p>EXPERT<br>SUPPORT</p>
    </div>
    <div class="promise-rule" style="left:237px"></div>
    <div class="promise" style="left:285px">
      <svg viewBox="0 0 52 52" fill="none" stroke="#0b0b0b" stroke-width="2"><path d="M2 12l10-4 8 20-8 4zM50 12l-10-4-8 20 8 4z"/><path d="M12 32l12 10q4 3 7 0l9-10M20 16l8-2 8 4M26 20l8 8"/></svg>
      <p>TURNKEY<br>DELIVERY</p>
    </div>
  </section>

  <h1 class="headline-top">SOLUTIONSS THAT</h1>
  <h2 class="headline-main">KEEP WATER MOVING</h2>
  <p class="tagline">EXPERTISE. RELIABILITY. RESULTS.</p>

  <div class="industry-band">COMPLETE SOLUTIONS FOR THE WATER &amp; WASTEWATER INDUSTRY</div>

  <section class="offerings">
    <article class="offering o1">
      <div class="offering-visual visual-steel" role="img" aria-label="Blue split-case centrifugal pump"></div>
      <h3>PUMPS</h3>
      <p>Industry leading pumps<br>built for performance,<br>efficiency &amp; reliability.</p>
    </article>
    <article class="offering o2">
      <div class="offering-visual visual-steel" role="img" aria-label="Blue industrial electric motor"></div>
      <h3>MOTORS</h3>
      <p>High efficiency motors<br>engineered for durability<br>and long life.</p>
    </article>
    <article class="offering o3">
      <div class="offering-visual visual-grey" role="img" aria-label="Grey positive displacement blower"></div>
      <h3>BLOWERS</h3>
      <p>Aeris PD positive displacement<br>blowers for reliable, energy<br>efficient performance.</p>
    </article>
    <article class="offering o4">
      <div class="offering-visual visual-drive" role="img" aria-label="Variable frequency drive cabinet with keypad"></div>
      <h3>VFD &amp; CONTROLS</h3>
      <p>Precision control and<br>energy savings through<br>advanced VFD solutions.</p>
    </article>
    <article class="offering o5">
      <div class="offering-visual visual-steel" role="img" aria-label="Blue flanged valve with pneumatic actuator"></div>
      <h3>AUTOMATION &amp; VALVES</h3>
      <p>Smart automation and<br>reliable valves for optimized<br>system performance.</p>
    </article>
    <article class="offering o6">
      <div class="offering-visual visual-steel" style="width:120px" role="img" aria-label="Icon of a hand holding a gear with a water drop"></div>
      <h3>TURNKEY SOLUTIONS</h3>
      <p>Complete systems de-<br>signed, integrated and sup-<br>ported by Harborline.</p>
    </article>
  </section>

  <footer>
    <div class="footer-water" role="img" aria-label="Deep blue water surface with bubbles"></div>
    <svg class="service-pin" viewBox="0 0 46 46"><circle cx="23" cy="23" r="22" fill="#2aa9e6" stroke="#fff" stroke-width="2"/><path d="M23 36s-9-9-9-15a9 9 0 0 1 18 0c0 6-9 15-9 15z" fill="#24398a"/><circle cx="23" cy="21" r="3.5" fill="#2aa9e6"/></svg>
    <div class="service-label">SERVICING</div>
    <div class="service-states">VIRGINIA | NORTH CAROLINA | MARYLAND | DELAWARE</div>
    <div class="footer-rule" style="left:471px"></div>
    <div class="site-url">www.<span>harborline-flow</span>.com</div>
    <div class="footer-rule" style="left:786px"></div>
    <div class="partner-lead">YOUR PARTNER FOR</div>
    <div class="partner-line">A BETTER FLOW FORWARD</div>
  </footer>
</main>
</body>
</html>
```